Used Car Dealer seeks an Amazing Business Card Design

We are looking for a business card design that incorporates our logo and grabs the attention of anyone we give the business card to.

Looking to use the same colors as the logo. Our Logo choice is the black background with Red and Silver/Grey Lettering.

We also would like to see some embossed designs.

Target Market(s)

Used Car Buyers, Automotive, Auto

Industry/Entity Type

Automotive

Contact Information for Business Card

BVEL7K
Gordon Whitlock
482 Tarrow Lane
Suite 207
Roswell, GA 30075
Office (770) 555-0142
Cell (770) 555-0187
bvel7kga@quellmail.com
www.bvel7kga.com

Colors
ffffff
ee3036

Requirements
Must have
• Must include our logo (Black Background with Red and Silver/Grey Lettering)
Nice to have
• Embossed Design. Can be Single or Double Sided.

```html
<!DOCTYPE html>
<html lang="en">
<head>
<meta charset="utf-8">
<title>BVEL7K Business Card</title>
<link href="https://fonts.googleapis.com/css2?family=Arimo:wght@400&display=swap" rel="stylesheet">
<style>
  :root {
    --page: #fdfdfd;
    --caption: #444444;
    --card: #000000;
    --text: #ffffff;
    --silver: #c9c9cc;
    --gold: #9a8b2b;
    --gold-deep: #5e5418;
    --label-ink: #2a2a10;
  }
  * { margin: 0; padding: 0; box-sizing: border-box; }
  html, body {
    width: 1200px; height: 1200px; overflow: hidden;
    background: var(--page);
    font-family: "Arimo", Arial, sans-serif;
  }
  .canvas { position: relative; width: 1200px; height: 1200px; }
  .caption {
    position: absolute; top: 256px; left: 0; width: 1200px;
    text-align: center; color: var(--caption);
    font-size: 32px; line-height: 38px;
  }
  .card {
    position: absolute; left: 151px; top: 399px;
    width: 898px; height: 538px;
    background: var(--card); overflow: hidden; color: var(--text);
  }
  .brand {
    position: absolute; left: 62px; top: 122px;
    font-size: 70px; line-height: 1; color: var(--silver);
    letter-spacing: 1px;
  }
  .gauge-art {
    position: absolute; left: 581px; top: 13px;
    width: 272px; height: 280px; border-radius: 50%;
    background: radial-gradient(circle at 45% 60%, #ffb23a 0%, #d85a10 12%, #6a1a05 38%, #1a0500 62%, #000000 75%);
  }
  .person { position: absolute; left: 46px; top: 302px; }
  .person-name { font-size: 37px; line-height: 44px; }
  .person-mobile { font-size: 20px; line-height: 24px; margin-top: 12px; }
  .contact-row {
    position: absolute; display: flex; align-items: center;
    font-size: 19px; line-height: 22px; white-space: nowrap;
  }
  .tag {
    display: inline-flex; align-items: center; justify-content: center;
    width: 16px; height: 16px; margin-right: 11px;
    background: var(--gold); color: var(--label-ink);
    font-size: 13px; line-height: 1;
  }
  .row-phone { left: 404px; top: 309px; }
  .row-email { left: 606px; top: 309px; }
  .row-address { left: 404px; top: 350px; }
  .row-web { left: 404px; top: 391px; }
  .racing-band {
    position: absolute; left: 0; top: 455px; width: 898px; height: 34px;
    background: linear-gradient(180deg, var(--gold) 0%, var(--gold-deep) 100%);
  }
</style>
</head>
<body>
<div class="canvas">
  <p class="caption">Single Sided Business Card<br>with Embossed Logo</p>

  <section class="card">
    <div class="brand">BVEL7K</div>
    <div class="gauge-art" role="img" aria-label="Glowing orange tachometer with needle near 8"></div>

    <div class="person">
      <div class="person-name">Gordon Whitlock</div>
      <div class="person-mobile">Mobile (770) 555-0187</div>
    </div>

    <div class="contact-row row-phone"><span class="tag">T</span>(770) 555-0142</div>
    <div class="contact-row row-email"><span class="tag">E</span>bvel7kga@quellmail.com</div>
    <div class="contact-row row-address"><span class="tag">A</span>482 Tarrow Lane, Suite 207, Roswell, GA 30075</div>
    <div class="contact-row row-web"><span class="tag">W</span>www.bvel7kga.com</div>

    <div class="racing-band" role="img" aria-label="Gold and black checkered racing flag strip"></div>
  </section>
</div>
</body>
</html>
```